Law Firm Logo and Business Card Design

I need a logo and business card design for a law firm I just started. The law firm is named Law Office of Renata M. Colbrook, LLC. The type of law I practice is Family Law, which includes divorce, custody, child support, alimony, property division, and the like. I would like to see designs that are unique and modern, yet sophisticated. I would also like to use the logo/design for my letterhead. I am not opposed to using some form of the scales of justice although I'd like something other than the typical, old fashioned scales of justice. I had considered a house made out of puzzle pieces with one puzzle piece pulled away from the others, with the logo text reading "Putting your life back together, one piece at a time." However, I don't want that particular design to look juvenile. I also would not be opposed to some form of my initials on the logo -- my initials are RMC. I am open to any other ideas you may have. I would like to see raised designs/lettering, and/or metallic finish. I like the colors black, white, gold, silver, and/or teal.

```html
<!DOCTYPE html>
<html lang="en">
<head>
<meta charset="utf-8">
<title>Law Office of Renata M. Colbrook, LLC — Business Card</title>
<link rel="stylesheet" href="https://fonts.googleapis.com/css2?family=Carlito:wght@400;700&family=Nunito:wght@700&display=swap">
<style>
  :root {
    --stage: #000000;
    --card-top: #e4e4e6;
    --card-mid: #ffffff;
    --brand-red: #8b0d17;
    --mark-light: #f07a6a;
    --mark-mid: #c8141c;
    --mark-dark: #6e0209;
    --band-top: #e81e26;
    --band-bottom: #6e0209;
    --title-grey: #4a4a4a;
    --sub-grey: #555555;
    --white: #ffffff;
    --icon-red: #b0121b;
  }
  * { margin: 0; padding: 0; box-sizing: border-box; }
  html, body {
    width: 1200px; height: 999px; overflow: hidden;
    background: var(--stage);
    font-family: "Carlito", "Calibri", sans-serif;
  }
  .card {
    position: absolute; left: 75px; top: 199px;
    width: 1050px; height: 600px; overflow: hidden;
    background: linear-gradient(to bottom, var(--card-top) 0%, var(--card-mid) 38%, var(--card-mid) 100%);
  }
  .card-band { position: absolute; left: 0; top: 0; width: 1050px; height: 600px; }

  .brand-mark {
    position: absolute; left: 203px; top: 61px;
    width: 146px; height: 146px; border-radius: 50%;
    background: radial-gradient(circle at 28% 32%, var(--mark-light) 0%, var(--mark-mid) 45%, var(--mark-dark) 100%);
  }
  .brand-name {
    position: absolute; left: 362px; top: 94px;
    font-family: "Nunito", sans-serif; font-weight: 700;
    color: var(--brand-red); white-space: nowrap;
  }
  .brand-name .line-1 { display: block; font-size: 42px; line-height: 48px; }
  .brand-name .line-2 { display: block; font-size: 36px; line-height: 44px; }

  .person {
    position: absolute; left: 0; width: 1050px; top: 246px;
    text-align: center; white-space: nowrap;
  }
  .person-name {
    color: var(--title-grey); font-weight: 700; font-size: 64px; line-height: 70px;
  }
  .person-role {
    color: var(--sub-grey); font-size: 44px; line-height: 40px;
  }

  .address {
    position: absolute; left: 78px; top: 446px;
    color: var(--white); font-size: 30px; line-height: 36px; white-space: nowrap;
  }
  .divider {
    position: absolute; left: 524px; top: 416px; width: 2px; height: 160px;
    background: linear-gradient(to bottom, rgba(255,255,255,0), rgba(255,255,255,0.9) 50%, rgba(255,255,255,0));
  }
  .contacts {
    position: absolute; left: 619px; top: 418px; list-style: none;
    color: var(--white); font-size: 32px; line-height: 36px; white-space: nowrap;
  }
  .contacts li { display: flex; align-items: center; gap: 12px; }
  .contacts svg { width: 24px; height: 24px; flex: none; }
</style>
</head>
<body>
<main class="card">
  <svg class="card-band" viewBox="0 0 1050 600" aria-hidden="true">
    <defs>
      <linearGradient id="band" x1="0" y1="0" x2="0" y2="1">
        <stop offset="0" stop-color="#e81e26"/>
        <stop offset="1" stop-color="#6e0209"/>
      </linearGradient>
      <linearGradient id="swoosh" x1="0" y1="0" x2="1" y2="0">
        <stop offset="0" stop-color="#b9b7bb" stop-opacity="0"/>
        <stop offset="0.55" stop-color="#f6f6f6"/>
        <stop offset="1" stop-color="#7f7c83"/>
      </linearGradient>
    </defs>
    <path d="M0 366 Q470 420 1050 366 L1050 600 L0 600 Z" fill="url(#band)"/>
    <path d="M410 402 Q760 395 1050 337 L1050 362 Q760 400 410 402 Z" fill="url(#swoosh)"/>
    <path d="M420 404 Q760 402 1050 364" fill="none" stroke="#ffffff" stroke-width="3"/>
  </svg>

  <header>
    <span class="brand-mark"></span>
    <h1 class="brand-name"><span class="line-1">Law Office of Renata M.</span><span class="line-2">Colbrook, LLC</span></h1>
  </header>

  <section class="person">
    <p class="person-name">Title name</p>
    <p class="person-role">designation</p>
  </section>

  <p class="address">Add:&nbsp; Lorem ipsum dolor sit<br>amet, consectetur adipiscing<br>elit,Lorem ipsum dolor</p>

  <div class="divider"></div>

  <ul class="contacts">
    <li>
      <svg viewBox="0 0 24 24"><rect x="1" y="1" width="22" height="22" rx="4" fill="#fff"/><rect x="7" y="4" width="10" height="16" rx="2" fill="none" stroke="#b0121b" stroke-width="2"/><circle cx="12" cy="17" r="1" fill="#b0121b"/></svg>
      000-000-0000
    </li>
    <li>
      <svg viewBox="0 0 24 24"><rect x="6" y="1" width="12" height="9" fill="#fff"/><rect x="1" y="10" width="22" height="13" rx="2" fill="#fff"/><rect x="5" y="14" width="14" height="3" fill="#b0121b"/></svg>
      000-000-0000
    </li>
    <li>
      <svg viewBox="0 0 24 24"><rect x="1" y="4" width="22" height="17" rx="2" fill="#fff"/><path d="M3 7 L12 14 L21 7" fill="none" stroke="#b0121b" stroke-width="2"/></svg>
      abcd@colbrooklaw.com
    </li>
    <li>
      <svg viewBox="0 0 24 24"><rect x="1" y="1" width="22" height="22" rx="5" fill="#fff"/><circle cx="12" cy="12" r="3.5" fill="none" stroke="#b0121b" stroke-width="2"/><path d="M15.5 9 V14 Q15.5 16 17.5 16 Q19 16 19 12 A7 7 0 1 0 15 18.5" fill="none" stroke="#b0121b" stroke-width="2"/></svg>
      www.colbrooklaw.com
    </li>
  </ul>
</main>
</body>
</html>
```